Thistlewood Group Business Card Design

We are looking for a new business card design, we are not happy with our current design. We are a boutique management consulting firm and our clients are typically meridian 400 companies.

I have attached the current front and back that we have as well as a version of our logo that can be used. I am trying to get a higher resolution version of the logo file to upload to the project.

Target Market(s)

Meridian 400 companies are our primary client base. Financial services, life sciences, pharmaceuticals and telecom companies are

Industry/Entity Type

Management Consulting

Contact Information for Business Card

We are trying to communicate a high degree of professionalism, a somewhat minimalist perhaps with some air of whimsy (without overdoing it). Attached is the current design, front and back as well as logos. I like the current back of the card and assume we will keep the phrase the same.

From a color palette perspective, I prefer to stay with a gray scale as they are today.

Font styles to use
Sans Serif

Colors
1b1b1b
474747
ffffff

Requirements
Must have
• Two sided business card design. File format should be something that can be used outside of Photoshop like MS Publisher so that they can be edited with personal information.
• Font should be calibri or something very similar and should be available within MS Office
Should not have
• No other logos or graphics outside of the logo provided.

```html
<!DOCTYPE html>
<html lang="en">
<head>
<meta charset="utf-8">
<title>Thistlewood Group Business Card</title>
<link rel="stylesheet" href="https://fonts.googleapis.com/css2?family=Carlito:wght@400;700&family=Open+Sans:wght@600&display=swap">
<style>
  :root {
    --ink: #1b1b1b;
    --ink-soft: #474747;
    --paper: #ffffff;
    --paper-shade: #f4f4f4;
    --backdrop: #e6e6e6;
    --faint-mark: #efefef;
  }
  * { box-sizing: border-box; margin: 0; padding: 0; }
  html, body { width: 1200px; height: 900px; overflow: hidden; }
  body {
    background: var(--backdrop);
    font-family: "Carlito", "Calibri", sans-serif;
    color: var(--ink);
    position: relative;
  }
  .card {
    position: absolute;
    top: 298px;
    width: 530px;
    height: 303px;
    background: var(--paper);
    box-shadow: 0 6px 18px rgba(0,0,0,0.18);
    overflow: hidden;
  }
  /* Reverse side: tagline */
  .card-reverse { left: 45px; }
  .card-reverse .faint-circle {
    position: absolute;
    left: 40px; top: 10px;
    width: 230px; height: 230px;
    border-radius: 50%;
    background: var(--faint-mark);
  }
  .tagline {
    position: absolute;
    left: 0; right: 0; top: 78px;
    text-align: center;
    font-family: "Open Sans", "Segoe UI", sans-serif;
    font-weight: 600;
    font-size: 31px;
    line-height: 1.22;
    color: var(--ink-soft);
  }
  .web-address {
    position: absolute;
    left: 0; right: 0; bottom: 34px;
    text-align: center;
    font-family: "Open Sans", "Segoe UI", sans-serif;
    font-weight: 600;
    font-size: 12px;
    color: var(--ink-soft);
  }
  /* Front side: identity and contact */
  .card-front { left: 625px; background: var(--paper-shade); }
  .brand-band {
    position: absolute;
    left: 0; top: 0;
    width: 100%; height: 150px;
    background: var(--ink);
  }
  .brand-name {
    position: absolute;
    left: 58px; top: 40px;
    display: flex; align-items: center; gap: 14px;
    font-weight: 700;
    font-size: 62px;
    line-height: 1;
    color: var(--paper);
  }
  .brand-name .brand-dot {
    width: 22px; height: 22px;
    border-radius: 50%;
    background: var(--paper);
  }
  .brand-tm {
    position: absolute;
    right: 34px; top: 26px;
    font-size: 11px;
    color: var(--paper);
  }
  .contact {
    position: absolute;
    right: 24px; top: 160px;
    text-align: right;
    color: var(--ink);
  }
  .contact .person-name { font-size: 16px; font-weight: 400; text-transform: uppercase; letter-spacing: 0.3px; }
  .contact .role { font-size: 13px; line-height: 1.3; color: var(--ink-soft); }
  .contact .detail {
    display: flex; justify-content: flex-end; align-items: center; gap: 6px;
    font-size: 13.5px; line-height: 1.45;
  }
  .contact .detail:first-of-type { margin-top: 8px; }
  .contact svg { width: 10px; height: 10px; fill: var(--ink); }
  .company-address {
    position: absolute;
    left: 38px; top: 178px;
    font-size: 17px;
    line-height: 1.2;
    color: var(--ink);
  }
  .company-address .company-name { font-weight: 700; font-size: 18px; }
  .company-address .company-name span { font-weight: 400; font-size: 15px; }
</style>
</head>
<body>

  <section class="card card-reverse">
    <div class="faint-circle"></div>
    <p class="tagline">The preferred choice<br>for leadership's<br>top priorities</p>
    <p class="web-address">www.thistlewoodGroup.com</p>
  </section>

  <section class="card card-front">
    <div class="brand-band">
      <div class="brand-name"><span class="brand-dot"></span>Thistlewood</div>
      <span class="brand-tm">TM</span>
    </div>

    <div class="contact">
      <p class="person-name">Marcus Hale</p>
      <p class="role">Los Angeles Office</p>
      <p class="role">Managing Director</p>
      <p class="detail">206.555.0147
        <svg viewBox="0 0 10 10" aria-hidden="true"><path d="M1 3 Q5 0 9 3 L8 4.5 L6.5 4 L6.5 3 Q5 2.5 3.5 3 L3.5 4 L2 4.5 Z M2.5 5 H7.5 L8.5 9 H1.5 Z"/></svg>
      </p>
      <p class="detail">mhale@thistlewoodgroup.com
        <svg viewBox="0 0 10 10" aria-hidden="true"><path d="M0.5 2 H9.5 V8.5 H0.5 Z M1.5 3 L5 5.6 L8.5 3" stroke="#f4f4f4" stroke-width="0.8"/></svg>
      </p>
    </div>

    <address class="company-address" style="font-style: normal;">
      <p class="company-name">Thistlewood group<span>,Inc.</span></p>
      <p>Headquarters</p>
      <p>218 Larkspur Avenue</p>
      <p>Suite 210</p>
      <p>Cedar Harbor, WA 98120</p>
    </address>
  </section>

</body>
</html>
```